Food Packaging for Shaved/Snow Ice (frozen dessert)

Need packing design for 7 different flavor shaved ice blocks. Already have company logo and feature product elements. Need to incorporate logo and featured elements into the packaging design.
The company name in Hokkien language means flipping table which is incorporated in the company logo and featured products. There are total of 7 flavor products that needs design work, mango, strawberry, pineapple, milk tea, coffee, red bean and peanuts. The goal is to have a common packaging theme for all the flavors and incorporate the corresponding feature elements for each flavor.
The eps files are uploaded below. The packaging is a plastic wrapping/pouch type. Packaging size is 11.25cm width x 14cm legnth; on the back size, need to leave 6.9cm width x 7.8 length for food labeling. More info on product and packing can be found in the "product sample clarification.pdf."
Target Market(s)
The intended product audience is 16-35 years of age consumers.
Industry/Entity Type
Food Production
Requirements
Must have
- Incorporate the company logo and corresponding feature product element provided.

```html
<!DOCTYPE html>
<html lang="en">
<head>
<meta charset="utf-8">
<title>Tilt Ice — Shaved Ice Blocks Packaging Range</title>
<link rel="stylesheet" href="https://fonts.googleapis.com/css2?family=Gochi+Hand&display=swap">
<style>
  :root {
    --bg: #f8e4b8;
    --pouch: #ffffff;
    --pouch-shade: #e9e9ea;
    --ink: #1d1d1d;
    --seal-line: #5ec3e6;
    --peanut: #8b5a3c;
    --pineapple: #e07a28;
    --redbean: #58202b;
    --strawberry: #e8234a;
    --coffee: #5b2d1b;
    --mango: #f6c23a;
    --milktea: #bf8a73;
  }
  html, body {
    margin: 0;
    padding: 0;
    width: 1200px;
    height: 1200px;
    overflow: hidden;
    background: var(--bg);
  }
  .range {
    position: absolute;
    left: 11px;
    top: 480px;
    display: flex;
    gap: 12px;
  }
  .pouch {
    --flavor: var(--peanut);
    position: relative;
    width: 158px;
    height: 232px;
    background: linear-gradient(90deg, var(--pouch-shade) 0%, var(--pouch) 18%, var(--pouch) 82%, var(--pouch-shade) 100%);
    font-family: "Gochi Hand", cursive;
    color: var(--ink);
    overflow: hidden;
  }
  .pouch--peanut { --flavor: var(--peanut); }
  .pouch--pineapple { --flavor: var(--pineapple); }
  .pouch--redbean { --flavor: var(--redbean); }
  .pouch--strawberry { --flavor: var(--strawberry); }
  .pouch--coffee { --flavor: var(--coffee); }
  .pouch--mango { --flavor: var(--mango); }
  .pouch--milktea { --flavor: var(--milktea); }
  .pouch__seal {
    height: 26px;
    background: var(--flavor);
    border-bottom: 2px solid var(--seal-line);
  }
  .brand {
    display: flex;
    align-items: center;
    justify-content: center;
    gap: 5px;
    margin-top: 12px;
    font-size: 14px;
    line-height: 1;
  }
  .brand__dot {
    width: 10px;
    height: 10px;
    border: 2px solid var(--ink);
    border-radius: 50%;
  }
  .pouch__flavor {
    margin: 10px 8px 0;
    padding-bottom: 3px;
    border-bottom: 1px solid #9a9a9a;
    text-align: center;
    font-size: 16px;
    letter-spacing: 0.3px;
    white-space: nowrap;
  }
  .pouch__art {
    width: 96px;
    height: 58px;
    margin: 10px auto 0;
    background: linear-gradient(180deg, #f3f3f3, #dcdcdc);
    border-radius: 6px;
  }
  .pouch__product {
    position: absolute;
    bottom: 14px;
    width: 40px;
    height: 42px;
    background: radial-gradient(circle at 40% 35%, #fff6 0%, transparent 45%), var(--flavor);
    border-radius: 45% 45% 40% 40%;
  }
  .pouch__product--left { left: -6px; }
  .pouch__product--right { right: -6px; }
  .pouch__tagline {
    position: absolute;
    left: 0;
    right: 0;
    bottom: 30px;
    text-align: center;
    font-size: 9px;
    letter-spacing: 0.6px;
    transform: rotate(-8deg);
  }
  .pouch__weight {
    position: absolute;
    left: 0;
    right: 0;
    bottom: 10px;
    text-align: center;
    font-size: 7px;
  }
</style>
</head>
<body>
  <main class="range">
    <section class="pouch pouch--peanut">
      <div class="pouch__seal"></div>
      <div class="brand"><span class="brand__dot"></span><span>Tilt Ice</span></div>
      <h2 class="pouch__flavor" style="font-weight:400">PEANUTS FLAVOR</h2>
      <div class="pouch__art" role="img" aria-label="Line drawing of an elephant character tipping a little table of peanuts"></div>
      <div class="pouch__product pouch__product--left" role="img" aria-label="Peanuts"></div>
      <div class="pouch__product pouch__product--right" role="img" aria-label="Peanuts"></div>
      <p class="pouch__tagline">SHAVED ICE BLOCKS</p>
      <p class="pouch__weight">Net Wt 6.7oz (200g)</p>
    </section>
    <section class="pouch pouch--pineapple">
      <div class="pouch__seal"></div>
      <div class="brand"><span class="brand__dot"></span><span>Tilt Ice</span></div>
      <h2 class="pouch__flavor" style="font-weight:400">PINEAPPLE FLAVOR</h2>
      <div class="pouch__art" role="img" aria-label="Line drawing of a monkey character tipping a table of pineapple"></div>
      <div class="pouch__product pouch__product--left" role="img" aria-label="Pineapple pieces"></div>
      <div class="pouch__product pouch__product--right" role="img" aria-label="Pineapple pieces"></div>
      <p class="pouch__tagline">SHAVED ICE BLOCKS</p>
      <p class="pouch__weight">Net Wt 6.7oz (200g)</p>
    </section>
    <section class="pouch pouch--redbean">
      <div class="pouch__seal"></div>
      <div class="brand"><span class="brand__dot"></span><span>Tilt Ice</span></div>
      <h2 class="pouch__flavor" style="font-weight:400">RED BEAN FLAVOR</h2>
      <div class="pouch__art" role="img" aria-label="Line drawing of a character tipping a table of red beans"></div>
      <div class="pouch__product pouch__product--left" role="img" aria-label="Red beans"></div>
      <div class="pouch__product pouch__product--right" role="img" aria-label="Red beans"></div>
      <p class="pouch__tagline">SHAVED ICE BLOCKS</p>
      <p class="pouch__weight">Net Wt 6.7oz (200g)</p>
    </section>
    <section class="pouch pouch--strawberry">
      <div class="pouch__seal"></div>
      <div class="brand"><span class="brand__dot"></span><span>Tilt Ice</span></div>
      <h2 class="pouch__flavor" style="font-weight:400">STRAWBERRY FLAVOR</h2>
      <div class="pouch__art" role="img" aria-label="Line drawing of a rabbit character tipping a table of strawberries"></div>
      <div class="pouch__product pouch__product--left" role="img" aria-label="Strawberries"></div>
      <div class="pouch__product pouch__product--right" role="img" aria-label="Strawberries"></div>
      <p class="pouch__tagline">SHAVED ICE BLOCKS</p>
      <p class="pouch__weight">Net Wt 6.7oz (200g)</p>
    </section>
    <section class="pouch pouch--coffee">
      <div class="pouch__seal"></div>
      <div class="brand"><span class="brand__dot"></span><span>Tilt Ice</span></div>
      <h2 class="pouch__flavor" style="font-weight:400">COFFEE FLAVOR</h2>
      <div class="pouch__art" role="img" aria-label="Line drawing of a character tipping a table of coffee beans and a cup"></div>
      <div class="pouch__product pouch__product--left" role="img" aria-label="Coffee beans"></div>
      <div class="pouch__product pouch__product--right" role="img" aria-label="Coffee beans"></div>
      <p class="pouch__tagline">SHAVED ICE BLOCKS</p>
      <p class="pouch__weight">Net Wt 6.7oz (200g)</p>
    </section>
    <section class="pouch pouch--mango">
      <div class="pouch__seal"></div>
      <div class="brand"><span class="brand__dot"></span><span>Tilt Ice</span></div>
      <h2 class="pouch__flavor" style="font-weight:400">MANGO FLAVOR</h2>
      <div class="pouch__art" role="img" aria-label="Line drawing of a cat character tipping a table of mango"></div>
      <div class="pouch__product pouch__product--left" role="img" aria-label="Mango"></div>
      <div class="pouch__product pouch__product--right" role="img" aria-label="Mango"></div>
      <p class="pouch__tagline">SHAVED ICE BLOCKS</p>
      <p class="pouch__weight">Net Wt 6.7oz (200g)</p>
    </section>
    <section class="pouch pouch--milktea">
      <div class="pouch__seal"></div>
      <div class="brand"><span class="brand__dot"></span><span>Tilt Ice</span></div>
      <h2 class="pouch__flavor" style="font-weight:400;font-size:20px">MILK TEA</h2>
      <div class="pouch__art" role="img" aria-label="Line drawing of a crowned character tipping a table with a teapot"></div>
      <div class="pouch__product pouch__product--left" role="img" aria-label="Cup of milk tea"></div>
      <div class="pouch__product pouch__product--right" role="img" aria-label="Cup of milk tea"></div>
      <p class="pouch__tagline">SHAVED ICE BLOCKS</p>
      <p class="pouch__weight">Net Wt 6.7oz (200g)</p>
    </section>
  </main>
</body>
</html>
```